TAILORED EYECARE AND EYEWEAR
Tailor made for you
We Care About Your Eyecare
Harwell Optometrists is a leading professional Opticians whose focus is on clinical care first and foremost using state of the are equipment followed by supplying design led spectacles and contact lenses. Our website is www.halvornsight.co.uk.
We are looking to have a postcard designed which will market the idea in requirements, this also has to have a poster to match which will be displayed in the store.
Health
Our target audience is adults aged 40 years+, our ethos is about patient care. The practice is both professional, clinical and design led. We must communicate the professionalism, simplicity and care. The Postcard will be personalised, obviously the poster will not.
A postcard which is A5 in size (please see the attached PDF for sizing and what areas to leave blank on the reverse for the address etc.) On the front if using a bleed this needs to be 3mm all round. To make it really tailored we would like to include the patients name on the front, this could be in any true type font as long as you supply a copy of the font, so it really can match in with the design. The Posters we require will be based upon the postcard and can be the same but 2 different sizes one is 60" x 40" portrait and the other 30" x 20" portrait. These all need to be CMYK and at 300DPI.
Postcard size information
Company Logo
Contact Details
Design Brief
Postcard Back Text
Postcard Front Text updated 09-09-11
Optometrist of the year logo
Premium Lens Practice Logo
Tailors Dummy

```html
<!DOCTYPE html>
<html lang="en">
<head>
<meta charset="utf-8">
<title>Harwell Optometrists – Tailored Eyecare Postcard</title>
<link rel="stylesheet" href="https://fonts.googleapis.com/css2?family=Exo+2:ital,wght@0,400;1,400;1,600&display=swap">
<style>
  :root {
    --paper: #ffffff;
    --brand-blue: #1f7fc4;
    --brand-navy: #1d3f6b;
    --chart-grey: #dcdfe2;
    --eye-tone: #e4e6e9;
    --dummy-light: #eee6d8;
    --dummy-shade: #d9cdb8;
  }
  * { box-sizing: border-box; margin: 0; padding: 0; }
  html, body {
    width: 1200px; height: 835px; overflow: hidden;
    background: var(--paper);
  }
  .postcard {
    position: relative;
    width: 1200px; height: 835px;
    background: var(--paper);
    overflow: hidden;
    font-family: "Exo 2", sans-serif;
  }
  .eye-chart {
    position: absolute;
    left: 280px; top: 0;
    width: 560px; height: 835px;
    background: linear-gradient(180deg, rgba(220,223,226,0.6) 0%, rgba(232,234,236,0.35) 60%, rgba(255,255,255,0) 100%);
  }
  .eye-photo {
    position: absolute;
    left: 600px; top: 0;
    width: 600px; height: 440px;
    background: radial-gradient(ellipse at 62% 45%, var(--eye-tone) 0%, #f1f2f3 45%, rgba(255,255,255,0) 75%);
  }
  .tailors-dummy {
    position: absolute;
    left: 40px; top: 80px;
    width: 300px; height: 755px;
    background: linear-gradient(90deg, var(--dummy-shade) 0%, var(--dummy-light) 45%, var(--dummy-light) 60%, var(--dummy-shade) 100%);
  }
  .message {
    position: absolute;
    left: 420px; top: 205px;
    transform: rotate(-12deg);
    transform-origin: left top;
    text-transform: uppercase;
    font-style: italic;
    color: var(--brand-blue);
    white-space: nowrap;
  }
  .message span { display: block; }
  .headline {
    width: 660px;
    font-weight: 600;
    font-size: 44px;
    line-height: 1.1;
    text-align: center;
  }
  .body-copy {
    width: 620px;
    margin: 38px 0 0 30px;
    font-weight: 400;
    font-size: 26px;
    line-height: 1.08;
    text-align: center;
  }
  .tagline {
    margin: 44px 0 0 10px;
    font-weight: 400;
    font-size: 18px;
    letter-spacing: 0.3px;
  }
  .brand {
    position: absolute;
    left: 910px; top: 610px;
    color: var(--brand-navy);
    font-weight: 400;
  }
  .brand-dot {
    display: block;
    width: 52px; height: 52px;
    border-radius: 50%;
    background: var(--brand-blue);
    margin: 0 0 16px 10px;
  }
  .brand-name { display: block; font-size: 60px; line-height: 1; }
  .brand-sub { display: block; font-size: 28px; letter-spacing: 3px; margin-top: 6px; padding-left: 22px; }
</style>
</head>
<body>
  <main class="postcard">
    <div class="eye-chart" role="img" aria-label="Soft-focus optician's letter chart in pale grey"></div>
    <div class="eye-photo" role="img" aria-label="Faint close-up photograph of an eye fading into white"></div>
    <div class="tailors-dummy" role="img" aria-label="Photograph of a cream tailor's dummy on a dark stand"></div>

    <section class="message">
      <h1 class="headline"><span>Does your optician treat</span><span>you like a number?</span></h1>
      <p class="body-copy"><span>We don't, we listen and tailor eyecare</span><span>and eyewear for your needs - that's</span><span>why our patients keep coming back!</span></p>
      <p class="tagline">Tailored eyecare and eyewear at Harwell Optometrists</p>
    </section>

    <div class="brand">
      <span class="brand-dot"></span>
      <span class="brand-name">Harwell</span>
      <span class="brand-sub">OPTOMETRISTS</span>
    </div>
  </main>
</body>
</html>
```